Simple elegant feminine design - Going out on my own as a Mortgage Broker.
My thoughts are the following details on the Front, middle of the card possibly? Phone and email smaller font than my name?
Marnie Veltrin
Finance Specialist
p: 0438 215 962
e: marnie@veltrinlending.com.au
Bottom of the card
residential / commercial / equipment
I would like the Font in Rose Gold maybe white or black background? or Possibly a stone grey - are you able to do a few options? I'd like them embossed
Then I had an idea as a simple logo as per the attached if you get the idea in my scribble, my initials, Veltrin Lending that leads/follows into a circle? Thicker Font In Rose Gold, middle of the card at the back.
Very open to ideas though and what colour you think would look better with the Rose Gold.
Thanks so much for your help, I am not very creative and savvy with this stuff :-)
Industry/Entity Type
Finance
Contact Information for Business Card
Marnie Veltrin
p: 0438 215 962
Look and feel

```html
<!DOCTYPE html>
<html lang="en">
<head>
<meta charset="utf-8">
<title>Marnie's Business Cards</title>
<link rel="stylesheet" href="https://fonts.googleapis.com/css2?family=Kaushan+Script&family=Raleway:wght@500;600&display=swap">
<style>
  :root {
    --backdrop: #808080;
    --card-black: #0d0d0d;
    --card-black-edge: #1c1c1c;
    --card-white: #ffffff;
    --gold: #c9a24a;
    --gold-deep: #a8802f;
    --ink: #111111;
  }
  * { box-sizing: border-box; margin: 0; padding: 0; }
  html, body {
    width: 1200px; height: 1200px; overflow: hidden;
    background: var(--backdrop);
  }
  .canvas { position: relative; width: 1200px; height: 1200px; }

  .card {
    position: absolute;
    width: 660px; height: 394px;
    border-radius: 26px;
  }

  /* back of card */
  .card--back {
    left: 272px; top: 148px;
    background: radial-gradient(ellipse at 50% 45%, var(--card-black-edge), var(--card-black) 75%);
  }
  .brand {
    position: absolute; left: 0; right: 0; top: 160px;
    display: flex; align-items: center; justify-content: center; gap: 14px;
  }
  .brand__dot {
    width: 14px; height: 14px; border-radius: 50%;
    background: var(--gold);
  }
  .brand__name {
    font-family: "Raleway", sans-serif; font-weight: 600;
    font-size: 44px; letter-spacing: 1px;
    color: var(--gold);
  }
  .services {
    position: absolute; left: 0; right: 0; top: 182px;
    margin-top: 150px;
    text-align: center;
    font-family: "Raleway", sans-serif; font-weight: 600;
    font-size: 18px; letter-spacing: 0.5px;
    color: var(--gold);
  }

  /* front of card */
  .card--front {
    left: 278px; top: 660px;
    background: var(--card-white);
    text-align: center;
  }
  .person__name {
    margin-top: 70px;
    font-family: "Kaushan Script", cursive;
    font-size: 50px; line-height: 1;
    color: var(--ink);
    text-shadow: 2px 2px 0 var(--gold), -1px -1px 0 var(--gold), 1px -1px 0 var(--gold), -1px 1px 0 var(--gold);
  }
  .person__role {
    margin-top: 2px;
    font-family: "Raleway", sans-serif; font-weight: 500;
    font-size: 20px; color: var(--ink);
  }
  .contact { margin-top: 64px; }
  .contact__item {
    display: flex; flex-direction: column; align-items: center;
    margin-bottom: 16px;
    font-family: "Raleway", sans-serif; font-weight: 500;
    font-size: 20px; color: var(--ink);
  }
  .contact__icon {
    width: 26px; height: 26px; border-radius: 50%;
    background: var(--gold);
    display: flex; align-items: center; justify-content: center;
    margin-bottom: 4px;
  }
  .contact__icon svg { width: 14px; height: 14px; fill: var(--ink); }
</style>
</head>
<body>
<main class="canvas">

  <section class="card card--back" aria-label="Card back">
    <div class="brand">
      <span class="brand__dot"></span>
      <span class="brand__name">Veltrin Lending</span>
    </div>
    <p class="services">residential | commercial | equipment</p>
  </section>

  <section class="card card--front" aria-label="Card front">
    <h1 class="person__name">Marnie Veltrin</h1>
    <p class="person__role">Finance Specialist</p>
    <div class="contact">
      <div class="contact__item">
        <span class="contact__icon">
          <svg viewBox="0 0 24 24" aria-hidden="true"><path d="M6.6 10.8a15.1 15.1 0 0 0 6.6 6.6l2.2-2.2a1 1 0 0 1 1-.25 11.4 11.4 0 0 0 3.6.57 1 1 0 0 1 1 1V20a1 1 0 0 1-1 1A17 17 0 0 1 3 4a1 1 0 0 1 1-1h3.5a1 1 0 0 1 1 1c0 1.25.2 2.45.57 3.57a1 1 0 0 1-.25 1z"/></svg>
        </span>
        <span>0438 215 962</span>
      </div>
      <div class="contact__item">
        <span class="contact__icon">
          <svg viewBox="0 0 24 24" aria-hidden="true"><path d="M3 6h18v12H3z M3 6l9 7 9-7" stroke="#c9a24a" stroke-width="1.5"/></svg>
        </span>
        <span>marnie@veltrinlending.com.au</span>
      </div>
    </div>
  </section>

</main>
</body>
</html>
```